Unique and original Business Card for Financial Services Business

I have moved premises and need to change the detail on my business card so thought now is a good time for a re-design. Looking for something professional and modern with colours to fit in with out logo. Like the idea of foil or embossing if that works but not a must have but I do want something that stands out and that I could not design myself.

Once business card is designed I will also be looking to get letterhead and flyers done but want the business card concept in place first.

The majority of designs I am receiving are generic and template based. I am looking for something unique and original. We have some great design elements in our logo, think outside the box and show me something that stands out from the crowd.

Target Market(s)

Business Professionals

Industry/Entity Type

Finance

Contact Information for Business Card

Name: Delia Norwood Phone 0473 958 162 Address PO Box 8617 Mossvale NSW 2389 Email info@steadyharbourfinancialservices.com.au website www.steadyharbourfinancialservices.com.au

Font styles to use
Other font styles liked:
• Ralway

Requirements
Should not have
• No black backgrounds please

```html
<!DOCTYPE html>
<html lang="en">
<head>
<meta charset="utf-8">
<title>Steady Harbour Financial Services – Business Card</title>
<link rel="stylesheet" href="https://fonts.googleapis.com/css2?family=Arimo:wght@400&family=Raleway:wght@300;400&display=swap">
<style>
  :root {
    --stage: #e6e8e9;
    --teal: #0b8a95;
    --teal-deep: #005a75;
    --teal-bright: #07a3a3;
    --teal-soft: #2fb3b6;
    --ink: #2b2b2b;
    --paper: #ffffff;
  }
  * { box-sizing: border-box; margin: 0; padding: 0; }
  html, body {
    width: 1200px; height: 939px; overflow: hidden;
    background: var(--stage);
  }
  .stage { position: relative; width: 1200px; height: 939px; }

  .card {
    position: absolute;
    width: 620px; height: 354px;
    box-shadow: 0 6px 18px rgba(0,0,0,0.18);
    overflow: hidden;
  }

  /* Back of card */
  .card-back {
    left: 90px; top: 90px;
    background: linear-gradient(200deg, var(--teal-bright) 0%, var(--teal) 45%, var(--teal-deep) 100%);
    display: flex; align-items: center; justify-content: center;
  }
  .back-mark {
    display: flex; align-items: center; gap: 16px;
    font-family: "Raleway", sans-serif; font-weight: 400;
    font-size: 30px; letter-spacing: 2px; text-transform: uppercase;
    color: var(--teal-soft);
  }
  .back-mark .dot {
    width: 34px; height: 34px; border-radius: 50%;
    background: var(--teal-soft);
  }

  /* Front of card */
  .card-front {
    left: 490px; top: 495px;
    background: var(--paper);
  }
  .brand {
    position: absolute; right: 46px; top: 34px;
    display: flex; align-items: center; gap: 12px;
    font-family: "Raleway", sans-serif; font-weight: 300;
    color: var(--teal);
  }
  .brand .square { width: 40px; height: 40px; background: var(--teal); }
  .brand .name { font-size: 30px; line-height: 1; text-transform: uppercase; letter-spacing: 0.5px; }
  .brand .tagline { font-size: 15px; letter-spacing: 6px; margin-top: 6px; }

  .rule-top {
    position: absolute; left: 250px; right: 0; top: 128px;
    height: 2px; background: var(--teal);
  }

  .person {
    position: absolute; left: 40px; top: 150px;
    font-family: "Arimo", sans-serif;
  }
  .person .full-name {
    font-size: 30px; font-weight: 400; line-height: 1.15;
    color: var(--teal); letter-spacing: 0.5px;
    text-transform: uppercase;
  }
  .person .role { font-size: 16px; color: var(--ink); margin-top: 2px; letter-spacing: 0.5px; }
  .rule-name { width: 330px; height: 2px; background: var(--teal); margin-top: 6px; }

  .contacts {
    list-style: none; margin-top: 8px;
    font-family: "Arimo", sans-serif; font-size: 14.5px; color: var(--ink);
  }
  .contacts li { display: flex; align-items: center; gap: 8px; height: 22px; letter-spacing: 0.3px; }
  .contacts svg { width: 14px; height: 14px; fill: var(--teal); flex: none; }
</style>
</head>
<body>
<main class="stage">

  <section class="card card-back" aria-label="Back of business card">
    <div class="back-mark"><span class="dot"></span>Steady Harbour</div>
  </section>

  <section class="card card-front" aria-label="Front of business card">
    <div class="brand">
      <span class="square"></span>
      <div>
        <div class="name">Steady Harbour</div>
        <div class="tagline">Financial Services</div>
      </div>
    </div>
    <div class="rule-top"></div>

    <div class="person">
      <h1 class="full-name">Delia Norwood</h1>
      <p class="role">President</p>
      <div class="rule-name"></div>
      <ul class="contacts">
        <li>
          <svg viewBox="0 0 24 24"><path d="M6.6 10.8c1.4 2.8 3.8 5.1 6.6 6.6l2.2-2.2c.3-.3.7-.4 1-.2 1.1.4 2.3.6 3.6.6.6 0 1 .4 1 1V20c0 .6-.4 1-1 1C10.6 21 3 13.4 3 4c0-.6.4-1 1-1h3.5c.6 0 1 .4 1 1 0 1.3.2 2.5.6 3.6.1.3 0 .7-.2 1z"/></svg>
          0473 958 162
        </li>
        <li>
          <svg viewBox="0 0 24 24"><path d="M2 5h20v14H2z M2 5l10 8 10-8" fill="none" stroke="var(--teal)" stroke-width="2"/></svg>
          info@steadyharbourfinancialservices.com.au
        </li>
        <li>
          <svg viewBox="0 0 24 24"><circle cx="12" cy="12" r="9" fill="none" stroke="var(--teal)" stroke-width="2"/><path d="M3 12h18M12 3c3 3 3 15 0 18M12 3c-3 3-3 15 0 18" fill="none" stroke="var(--teal)" stroke-width="1.5"/></svg>
          www.steadyharbourfinancialservices.com.au
        </li>
        <li>
          <svg viewBox="0 0 24 24"><path d="M12 2a7 7 0 0 0-7 7c0 5 7 13 7 13s7-8 7-13a7 7 0 0 0-7-7zm0 9.5a2.5 2.5 0 1 1 0-5 2.5 2.5 0 0 1 0 5z"/></svg>
          PO Box 8617 Mossvale NSW 2389
        </li>
      </ul>
    </div>
  </section>

</main>
</body>
</html>
```